Surface Protection company needs cards

We are a New Zealand company that will apply nanotechnology coatings on surfaces to prevent growth and spread of bacteria, viruses, mold etc with a sprayer. We deal with large corporates, airlines, hospitals and schools so we are after a new modern, simple and clean look that will have great visual impact.
We a company that is focused on prevention and protection.

Company name, Vela Shield

Subtext, Antimicrobial Surface Protection

Logo, VS

Target Market(s)

Hospitals, Transport agencies, Airlines, Corporate entities

Contact Information for Business Card

Company name, VelaShield
Logo, VS

Garth Ormsby
velashieldnz@postkite.example
+64219302648
www.velashield.example.nz

Requirements
Must have
• Simple clean look.
Nice to have
• We apply nano coatings so try and incorporate this into a theme somehow

```html
<!DOCTYPE html>
<html lang="en">
<head>
<meta charset="utf-8">
<title>Vela Shield – Business Cards</title>
<link rel="stylesheet" href="https://fonts.googleapis.com/css2?family=Signika:wght@400;600;700&family=Montserrat:wght@600&display=swap">
<style>
  :root {
    --canvas: #a3a3a3;
    --card-white: #ffffff;
    --indigo: #2e3192;
    --indigo-light: #3d41a8;
    --sky-deep: #4a9fdc;
    --sky-light: #e9f3fb;
    --band-blue: #1477c4;
    --text-dark: #1d1d1f;
    --text-grey: #5a5a5e;
    --rule-grey: #c9c9cc;
    --divider: #8e8e92;
  }
  * { box-sizing: border-box; margin: 0; padding: 0; }
  html, body { width: 1200px; height: 800px; overflow: hidden; }
  body {
    background: var(--canvas);
    font-family: "Signika", "Trebuchet MS", sans-serif;
    display: flex;
    align-items: center;
    justify-content: center;
    gap: 40px;
  }
  .card {
    position: relative;
    width: 540px;
    height: 309px;
    overflow: hidden;
    box-shadow: 0 10px 28px rgba(0,0,0,0.28);
  }

  /* ---------- Front ---------- */
  .card--front { background: var(--card-white); }
  .front__brand {
    position: absolute;
    left: 0; top: 0;
    width: 250px; height: 250px;
    display: flex; flex-direction: column;
    align-items: center; justify-content: center;
    gap: 14px;
  }
  .brand-mark { display: flex; align-items: center; gap: 10px; }
  .brand-mark__dot {
    width: 22px; height: 22px; border-radius: 50%;
    background: var(--indigo);
  }
  .brand-mark__name {
    font-weight: 700; font-size: 27px; letter-spacing: 0.5px;
    color: var(--indigo);
  }
  .brand-tagline {
    text-align: center; font-size: 16px; line-height: 1.3;
    color: var(--text-dark); font-weight: 400;
  }
  .front__divider {
    position: absolute; left: 262px; top: 60px;
    width: 1.5px; height: 128px; background: var(--divider);
  }
  .front__contact {
    position: absolute; left: 292px; top: 66px; right: 18px;
  }
  .contact__name {
    font-size: 22px; font-weight: 600; color: var(--text-grey);
    margin-bottom: 8px;
  }
  .contact__row {
    display: flex; align-items: center; gap: 6px;
    font-size: 15px; color: var(--text-grey); height: 24px;
  }
  .contact__row svg { width: 14px; height: 14px; flex: none; }
  .contact__row--address { margin-top: 12px; }
  .contact__fill { flex: 1; height: 1px; background: var(--rule-grey); margin-left: 4px; align-self: flex-end; margin-bottom: 6px; }
  .contact__rule { height: 1px; background: var(--rule-grey); margin: 16px 0 0 30px; }
  .url-band {
    position: absolute; left: 0; right: 0;
    display: flex; align-items: center; justify-content: center;
    font-family: "Montserrat", "Arial", sans-serif; font-weight: 600;
    color: #fff; letter-spacing: 7px; font-size: 14px;
  }
  .card--front .url-band {
    bottom: 16px; height: 30px;
    background: linear-gradient(90deg, var(--indigo) 0%, var(--indigo-light) 50%, var(--indigo) 100%);
  }

  /* ---------- Back ---------- */
  .card--back {
    background: radial-gradient(ellipse 60% 70% at 50% 45%, #ffffff 0%, var(--sky-light) 35%, var(--sky-deep) 100%);
  }
  .back__brand {
    position: absolute; left: 0; right: 0; top: 72px;
    display: flex; flex-direction: column; align-items: center; gap: 10px;
  }
  .back__brand .brand-mark__name { font-size: 30px; }
  .back__brand .brand-tagline { font-size: 14px; }
  .card--back .url-band {
    bottom: 28px; height: 30px; background: var(--band-blue);
  }
</style>
</head>
<body>

  <section class="card card--front" aria-label="Business card front">
    <div class="front__brand">
      <div class="brand-mark">
        <span class="brand-mark__dot"></span>
        <span class="brand-mark__name">VELA SHIELD</span>
      </div>
      <p class="brand-tagline">Antimicrobial<br>Surface Protection</p>
    </div>

    <div class="front__divider"></div>

    <div class="front__contact">
      <p class="contact__name">Garth Ormsby</p>
      <p class="contact__row">
        <svg viewBox="0 0 16 16" aria-hidden="true"><circle cx="8" cy="8" r="8" fill="#2e3192"/><path d="M5.2 4.2l1.4-.4.9 2-1 .8a5 5 0 0 0 2.9 2.9l.8-1 2 .9-.4 1.4c-3.3.3-6.9-3.3-6.6-6.6z" fill="#fff"/></svg>
        : +6 42193 02648
      </p>
      <p class="contact__row">
        <svg viewBox="0 0 16 16" aria-hidden="true"><rect x="1" y="4" width="14" height="10" rx="1" fill="#2e3192"/><path d="M1.5 4.5L8 10l6.5-5.5" stroke="#fff" stroke-width="1.2" fill="none"/></svg>
        : velashieldnz@postkite.example
      </p>
      <p class="contact__row contact__row--address">
        <svg viewBox="0 0 16 16" aria-hidden="true"><path d="M8 1a5 5 0 0 0-5 5c0 3.8 5 9 5 9s5-5.2 5-9a5 5 0 0 0-5-5z" fill="#2e3192"/><circle cx="8" cy="6" r="2" fill="#fff"/></svg>
        : Office Address Here
        <span class="contact__fill"></span>
      </p>
      <div class="contact__rule"></div>
    </div>

    <div class="url-band">www.velashield.example.nz</div>
  </section>

  <section class="card card--back" aria-label="Business card back">
    <div class="back__brand">
      <div class="brand-mark">
        <span class="brand-mark__dot"></span>
        <span class="brand-mark__name">VELA SHIELD</span>
      </div>
      <p class="brand-tagline">Antimicrobial<br>Surface Protection</p>
    </div>
    <div class="url-band">www.velashield.example.nz</div>
  </section>

</body>
</html>
```